依頼概要
■ 依頼の目的/概要

弊社は「カード選びナビ広場 http://www.hoshizora-cardnavi.com/ 」というクレジットカードの比較サイトを運営しています。
今回はこのカード選びナビ広場のトップページのサイトデザインリニューアルをお願いします。

現在、サイト内( http://www.hoshizora-cardnavi.com/ )にある素材は自由に使って頂いて構いません。
既存のデザインを残しつつデザインをしていただいても
逆に完全新規にデザインをしていただいても構いません。
最終的なクオリティが高ければOKです。
素材サイトで何か素材を購入すればよりクオリティが高くなるのであれば
別途素材の購入も検討します。
その際はメッセージでご連絡ください。

■コーディング不要
コーディングは不要なので、デザインのみでOKです。

■ 希望するウェブデザイン

サイト訪問者が楽しくクレジットカードを選んだり
クレジットカードについての知識を学んだりできるようなデザインが希望です。
逆にサイト訪問者が堅苦しく感じてしまうようなデザインは避けたいです。
既存サイトでは下記URLのようなサイトデザインが好みです。

http://www.mz.tobira-net.com/mobile/index.html?bid=mz_gn_0007
http://www.mirumart.co.jp/kuruma/index.html?ca=top_glo_009
http://store.fenlow.com/jp/
http://store.tavix.jp/Special/Compare/Computer/Relmo/index.html

また「クレジットカード」で検索して1ページ目に出てくるサイトには
綺麗なサイトが多いので、こちらも参考にして頂きたいです。

【サイズの横幅について】

現在の横幅はぴったり950pxですが、
980px前後までであれば、横幅が大きくなっても構いません。
横幅が現在よりも小さくなるのは不可です。

ただし、ヘッダー部分とフッター部分は下記サイトのように横全体に広がっているデザインが希望です。
http://www.qrt.co.jp/ordercard/index.html

■ 納品ファイルの希望

第一希望 フォトショップ形式 + BMP形式
第二希望 イラストレーター形式 + BMP形式

■ 進め方

弊社の希望するイメージに近い提案を1つ(場合によって複数)選択させて頂きます。希望に近づけるために、修正要望を個別にさせて頂くこともあります。コンペ方式のため、修正後に当選されない場合も、どうかご了承ください。

■ その他/注意点

選択させて頂いたウェブデザインの著作権(財産権)等の扱いはTezukuri利用規約に従い、弊社に譲渡をお願いします。フォントや画像素材などを利用する場合は上記利用用途に使用できることを確認し、第三者の知的財産権等に注意して下さい。
■リニューアルによる変更点
今回のリニューアルではデザイン面だけでなくシステム面も強化するため
トップページのデザインが一部変更になります。
変更点は添付ファイルにまとめました。
なので現在のトップページのデザイン( http://www.hoshizora-cardnavi.com/
ではなく添付ファイル内のデザインを元にデザインをしてください。

```html
<!DOCTYPE html>
<html lang="ja">
<head>
<meta charset="utf-8">
<title>カード選びナビ広場 | ライフスタイルに合ったお得なクレジットカードを探そう</title>
<link rel="stylesheet" href="https://fonts.googleapis.com/css2?family=Noto+Sans+JP:wght@400;700&family=M+PLUS+Rounded+1c:wght@700;800&display=swap">
<style>
:root{
  --blue:#1b6fc2;
  --blue-dark:#0f4f96;
  --blue-light:#e8f3fc;
  --blue-line:#9cc6ea;
  --sky:#cfe6f8;
  --orange:#f28a00;
  --orange-dark:#d96a00;
  --green:#3a9b2c;
  --red:#d8242b;
  --text:#333;
  --muted:#777;
  --line:#d5d5d5;
  --bg:#f2f7fb;
  --white:#fff;
}
*{box-sizing:border-box;margin:0;padding:0}
html,body{width:1200px;height:3560px;overflow:hidden}
body{background:var(--bg);font-family:"Noto Sans JP",sans-serif;color:var(--text);font-size:12px;line-height:1.5}
ul{list-style:none}

/* header */
.site-header{height:150px;background:linear-gradient(#ffffff,#e4f1fb);border-bottom:4px solid var(--blue)}
.header-inner{width:1000px;margin:0 auto;position:relative;height:146px}
.brand{position:absolute;left:0;top:18px;display:flex;align-items:center;gap:10px}
.brand-mark{width:40px;height:40px;border-radius:50%;background:var(--orange)}
.brand-name{font-family:"M PLUS Rounded 1c",sans-serif;font-weight:800;font-size:30px;color:var(--blue)}
.tagline{position:absolute;left:330px;top:30px;font-size:15px;color:var(--blue-dark);font-weight:700}
.search{position:absolute;right:0;top:20px;display:flex}
.search span{width:170px;height:26px;border:1px solid var(--blue-line);background:#fff}
.search b{width:46px;height:26px;background:var(--blue);color:#fff;font-size:12px;text-align:center;line-height:26px}
.global-nav{position:absolute;left:0;right:0;top:92px;display:flex;gap:6px}
.global-nav li{flex:1;height:46px;border-radius:8px 8px 0 0;background:linear-gradient(#4e9ee0,var(--blue));color:#fff;font-weight:700;font-size:14px;display:flex;align-items:center;justify-content:center;gap:8px}
.global-nav li.current{background:linear-gradient(#ffb13c,var(--orange))}
.global-nav i{width:16px;height:16px;border-radius:50%;background:#fff;opacity:.8}

/* layout */
.container{width:1000px;margin:10px auto 0;display:flex;gap:20px;height:3090px}
.main{width:680px}
.side{width:300px}
.box{background:#fff;border:1px solid var(--blue-line);border-radius:6px;margin-bottom:10px;overflow:hidden}
.sec-head{height:40px;background:linear-gradient(#3c8fd8,var(--blue));color:#fff;font-weight:700;font-size:15px;display:flex;align-items:center;padding-left:14px;gap:10px}
.sec-head::before{content:"";width:18px;height:18px;border-radius:50%;background:#fff}
.sec-head em{font-style:normal;background:var(--orange);padding:2px 8px;border-radius:3px;font-size:13px}
.ph{border-radius:4px}

/* intro */
.intro{height:140px;padding:16px 20px;display:flex;gap:20px;background:linear-gradient(#fff,var(--blue-light))}
.intro p{font-size:13px;line-height:2;flex:1}
.intro p strong{color:var(--red)}
.intro .ph{width:200px;height:108px;background:linear-gradient(135deg,#f6c45a,#7cb8e8 60%,#e56a8a)}

/* news */
.news{height:120px;padding:12px 20px}
.news li{font-size:12px;padding:2px 0;border-bottom:1px dotted var(--line)}
.news time{color:var(--blue);margin-right:14px}

/* popular */
.popular{height:460px}
.pop-grid{display:flex;gap:10px;padding:14px}
.pop-card{flex:1;border:1px solid var(--line);border-radius:6px;text-align:center;padding-bottom:8px}
.fee{background:var(--green);color:#fff;font-weight:700;font-size:12px;padding:4px 0;border-radius:5px 5px 0 0}
.fee b{display:block;font-size:16px}
.pop-card h3{font-size:13px;color:var(--blue);margin:8px 0 6px}
.pop-card .ph{width:130px;height:82px;margin:0 auto 8px;background:linear-gradient(135deg,#c9d8e6,#6f8fb0)}
.pop-card:nth-child(2) .ph{background:linear-gradient(135deg,#f4d47c,#c48a2a)}
.pop-card:nth-child(3) .ph{background:linear-gradient(135deg,#f0f0f0,#a8a8a8)}
.pop-card:nth-child(4) .ph{background:linear-gradient(135deg,#5c6e88,#1d2a40)}
.pop-card p{font-size:11px;text-align:left;padding:0 8px;color:var(--muted);height:52px}
.more-btn{display:inline-block;margin-top:6px;background:var(--orange);color:#fff;font-size:11px;font-weight:700;padding:3px 14px;border-radius:12px}
.pop-sub{display:flex;gap:10px;padding:0 14px}
.pop-sub li{flex:1;height:70px;border:1px solid var(--line);border-radius:6px;display:flex;align-items:center;gap:10px;padding:8px;font-size:11px}
.pop-sub .ph{width:60px;height:46px;flex:none;background:linear-gradient(135deg,#e45656,#f1b24a)}
.pop-sub li:nth-child(2) .ph{background:linear-gradient(135deg,#3ba06a,#9ed36b)}

/* feature */
.feature{height:320px}
.feature h4{margin:12px 14px 8px;font-size:13px;color:var(--orange-dark);border-left:4px solid var(--orange);padding-left:8px}
.feat-grid{display:grid;grid-template-columns:repeat(4,1fr);gap:10px 12px;padding:0 14px}
.feat-grid li{border:1px solid var(--line);border-radius:4px;padding:6px;display:flex;gap:6px;font-size:11px;height:100px}
.feat-grid .ph{width:64px;height:84px;flex:none;background:linear-gradient(#a8d4f2,#6aa8d6)}
.feat-grid li:nth-child(even) .ph{background:linear-gradient(#f6f0d0,#d8c890)}
.link-more{text-align:right;font-size:11px;color:var(--blue);padding:8px 14px}

/* search */
.search-box{height:700px;margin-top:10px}
.search-body{padding:14px 20px}
.search-lead{font-size:12px;color:var(--blue);margin-bottom:8px}
.group{margin-bottom:10px}
.group h5{font-size:12px;color:#fff;background:var(--blue);display:inline-block;padding:1px 10px;border-radius:3px;margin-bottom:5px}
.group h5.orange{background:var(--orange)}
.group h5.green{background:var(--green)}
.checks{display:grid;grid-template-columns:repeat(3,1fr);gap:3px 10px}
.checks li{font-size:12px;display:flex;align-items:center;gap:6px}
.checks li::before{content:"";width:12px;height:12px;border:1px solid #999;background:#fff;flex:none}
.select{display:inline-block;width:180px;height:22px;border:1px solid #999;background:#fff;font-size:12px;padding-left:6px}
.submit{margin:16px auto 0;width:260px;height:56px;border-radius:8px;background:linear-gradient(#ffb13c,var(--orange-dark));color:#fff;font-weight:700;font-size:17px;display:flex;align-items:center;justify-content:center}
.hit{text-align:center;font-size:12px;margin-top:6px}
.hit b{color:var(--red);font-size:18px}
.search-note{text-align:center;font-size:11px;color:var(--blue);margin-top:8px}

/* versus */
.versus{height:1080px;margin-top:10px}
.vs-row{display:flex;align-items:center;gap:16px;margin:14px;padding:14px;border:1px solid var(--line);border-radius:6px;height:236px;background:linear-gradient(#fff,#f7fbfe)}
.vs-label{width:110px;font-weight:700;font-size:15px;color:var(--blue-dark);line-height:1.6}
.vs-card{flex:1;text-align:center;font-size:11px}
.vs-card .ph{width:150px;height:94px;margin:0 auto 8px;background:linear-gradient(135deg,#9bc4e6,#3a78b8)}
.vs-card.b .ph{background:linear-gradient(135deg,#f2b6b6,#c84b4b)}
.vs-mark{font-family:"M PLUS Rounded 1c",sans-serif;font-weight:800;font-size:34px;color:var(--red)}
.detail{display:inline-block;margin-top:6px;background:var(--orange);color:#fff;font-weight:700;padding:4px 16px;border-radius:4px}
.vs-foot{text-align:center;font-size:11px;color:var(--blue);padding:10px}

/* side */
.ad-platinum{height:140px;background:linear-gradient(135deg,#2a2a34,#6c6c7c);border-radius:6px;margin-bottom:10px;position:relative}
.ad-platinum span{position:absolute;left:16px;bottom:14px;color:#fff;font-weight:700;font-size:14px}
.cat{height:690px}
.cat h4{margin:10px 12px 6px;font-size:13px;color:var(--orange-dark);border-bottom:2px solid var(--orange);padding-bottom:2px}
.cat ul{margin:0 12px}
.cat li{font-size:12px;padding:4px 0 4px 14px;border-bottom:1px dotted var(--line);position:relative}
.cat li::before{content:"";position:absolute;left:2px;top:10px;border:4px solid transparent;border-left:5px solid var(--blue)}
.brand-tiles{display:grid;grid-template-columns:1fr 1fr;gap:8px;margin:10px 12px}
.brand-tiles div{height:40px;border:1px solid var(--line);border-radius:4px;display:flex;align-items:center;justify-content:center;gap:6px;font-weight:700;font-size:12px;color:var(--blue-dark)}
.brand-tiles div::before{content:"";width:14px;height:14px;background:var(--blue-line)}
.ad-campaign{height:110px;border-radius:6px;background:linear-gradient(#fff3dc,#f7c56a);margin-bottom:10px;padding:12px;position:relative}
.ad-campaign b{color:var(--red);font-size:22px;display:block}
.ad-campaign span{font-size:12px;font-weight:700}
.rank{height:590px}
.rank li{display:flex;gap:8px;padding:8px 12px;border-bottom:1px dotted var(--line);font-size:11px;height:84px}
.rank .no{width:22px;height:22px;border-radius:50%;background:var(--orange);color:#fff;font-weight:700;text-align:center;line-height:22px;flex:none}
.rank .ph{width:76px;height:48px;flex:none;background:linear-gradient(135deg,#c8dcef,#5c8ec0)}
.rank li:nth-child(even) .ph{background:linear-gradient(135deg,#f3dd9e,#c99b3a)}
.rank strong{color:var(--blue);display:block}
.ad-gold{height:520px;border:1px solid var(--line);background:#fff;border-radius:6px;padding:14px;text-align:center}
.ad-gold p{font-size:12px;font-weight:700;color:var(--blue-dark);margin-bottom:10px}
.ad-gold .ph{height:190px;background:linear-gradient(135deg,#f6e2a2,#b8892e)}
.ad-gold .name{margin-top:10px;font-size:13px;font-weight:700}

/* footer */
.pagetop{width:1000px;margin:0 auto;height:40px;text-align:right;font-size:11px;color:var(--blue);padding-top:12px}
.about{width:1000px;margin:0 auto;height:130px;background:#fff;border:1px solid var(--blue-line);border-radius:6px;padding:14px 20px;display:flex;gap:30px}
.about div{flex:1}
.about h6{font-size:14px;color:var(--blue);margin-bottom:6px}
.about p{font-size:11px;line-height:1.8}
.share{display:flex;gap:8px;align-items:flex-start}
.share span{width:26px;height:26px;border-radius:50%;background:var(--blue-line)}
.site-footer{position:absolute;left:0;top:3440px;width:1200px;height:120px;background:linear-gradient(var(--blue),var(--blue-dark));color:#fff}
.footer-inner{width:1000px;margin:0 auto;padding-top:30px;text-align:center}
.footer-inner ul{display:flex;justify-content:center;gap:26px;font-size:12px;margin-bottom:16px}
.footer-inner small{font-size:11px}
</style>
</head>
<body>
<header class="site-header">
  <div class="header-inner">
    <div class="brand"><span class="brand-mark"></span><span class="brand-name">カード選びナビ広場</span></div>
    <p class="tagline">ライフスタイルに合ったお得なクレジットカードを探そう!</p>
    <div class="search"><span></span><b>検索</b></div>
    <ul class="global-nav">
      <li class="current"><i></i>カテゴリから探す</li>
      <li><i></i>一覧表で比較</li>
      <li><i></i>ブログ</li>
      <li><i></i>クレジットカード知識と一覧</li>
    </ul>
  </div>
</header>

<div class="container">
  <main class="main">
    <section class="box intro">
      <p>カード選びナビ広場は、<strong>あなたのライフスタイルにぴったりのクレジットカード</strong>を見つけるための比較サイトです。年会費・ポイント還元率・特典などの条件から、お得な一枚をかんたんに探すことができます。</p>
      <div class="ph" role="img" aria-label="複数のクレジットカードを並べたイラスト"></div>
    </section>

    <section class="box news">
      <ul>
        <li><time>2013年2月28日</time>春の新規入会キャンペーン情報を更新しました</li>
        <li><time>2013年2月20日</time>ゴールドカード特集ページを追加しました</li>
        <li><time>2013年2月12日</time>ポイント還元率ランキングを更新しました</li>
        <li><time>2013年2月05日</time>学生向けカードの比較表を公開しました</li>
        <li><time>2013年1月28日</time>サイトの表示速度を改善しました</li>
      </ul>
    </section>

    <section class="box popular">
      <h2 class="sec-head"><em>年会費無料</em>当サイト人気クレジットカード</h2>
      <div class="pop-grid">
        <article class="pop-card"><div class="fee">年会費<b>永年無料</b></div><h3>ブルースカイカード</h3><div class="ph" role="img" aria-label="ブルースカイカードの券面"></div><p>ポイントが貯まりやすく初めての一枚におすすめです。</p><span class="more-btn">詳細を見る</span></article>
        <article class="pop-card"><div class="fee">年会費<b>初年度無料</b></div><h3>サンライズカード</h3><div class="ph" role="img" aria-label="サンライズカードの券面"></div><p>ショッピング保険付きで旅行にも安心の一枚です。</p><span class="more-btn">詳細を見る</span></article>
        <article class="pop-card"><div class="fee">年会費<b>条件付無料</b></div><h3>シルバーリーフカード</h3><div class="ph" role="img" aria-label="シルバーリーフカードの券面"></div><p>コンビニ利用でポイント最大3倍になります。</p><span class="more-btn">詳細を見る</span></article>
        <article class="pop-card"><div class="fee">年会費<b>10,000円</b></div><h3>ミッドナイトカード</h3><div class="ph" role="img" aria-label="ミッドナイトカードの券面"></div><p>空港ラウンジ無料など上質な特典が揃います。</p><span class="more-btn">詳細を見る</span></article>
      </div>
      <ul class="pop-sub">
        <li><div class="ph" role="img" aria-label="ポイントカードのイラスト"></div><span>電子マネー一体型でお買い物がもっと便利になるカードです。</span></li>
        <li><div class="ph" role="img" aria-label="電子マネーのイラスト"></div><span>ネット通販でポイント2倍、年会費無料の人気カードです。</span></li>
      </ul>
    </section>

    <section class="box feature">
      <h2 class="sec-head">クレジットカードを知る・特集</h2>
      <h4>おすすめ特集ピックアップ</h4>
      <ul class="feat-grid">
        <li><div class="ph" role="img" aria-label="海外旅行の風景写真"></div><span>海外旅行に強いカードの選び方</span></li>
        <li><div class="ph" role="img" aria-label="初心者マークのイラスト"></div><span>はじめてのクレジットカード入門</span></li>
        <li><div class="ph" role="img" aria-label="金庫のイラスト"></div><span>審査に通るためのポイント</span></li>
        <li><div class="ph" role="img" aria-label="ポイントのイラスト"></div><span>ポイント還元率を徹底比較</span></li>
        <li><div class="ph" role="img" aria-label="空港の写真"></div><span>マイルが貯まるカード特集</span></li>
        <li><div class="ph" role="img" aria-label="学生のイラスト"></div><span>学生におすすめのカード</span></li>
        <li><div class="ph" role="img" aria-label="鍵のイラスト"></div><span>不正利用から身を守る方法</span></li>
        <li><div class="ph" role="img" aria-label="買い物袋のイラスト"></div><span>ネット通販でお得なカード</span></li>
      </ul>
      <p class="link-more">▶ すべての特集を見る</p>
    </section>

    <section class="box search-box">
      <h2 class="sec-head">クレジットカードを条件から絞り込んで探す</h2>
      <div class="search-body">
        <p class="search-lead">条件にチェックを入れて「この条件で検索する」ボタンを押してください。</p>
        <div class="group"><h5>サービスで探す</h5>
          <ul class="checks"><li>年会費無料</li><li>ポイント高還元</li><li>マイルが貯まる</li><li>電子マネー対応</li><li>ETCカード発行</li><li>家族カード発行</li><li>即日発行</li><li>海外旅行保険</li><li>国内旅行保険</li><li>ショッピング保険</li><li>空港ラウンジ</li><li>キャッシング可</li></ul></div>
        <div class="group"><h5 class="orange">国際ブランド</h5>
          <ul class="checks"><li>VELA</li><li>MERIDIAN</li><li>KSN</li><li>Atlas Prestige</li><li>Dorian Club</li></ul></div>
        <div class="group"><h5 class="green">利用シーン</h5>
          <ul class="checks"><li>コンビニ</li><li>スーパー</li><li>ネット通販</li><li>ガソリンスタンド</li><li>百貨店</li><li>携帯電話料金</li><li>公共料金</li><li>旅行・ホテル</li><li>レストラン</li></ul></div>
        <div class="group"><h5>カードの種類</h5>
          <ul class="checks"><li>一般カード</li><li>ゴールドカード</li><li>プラチナカード</li><li>学生カード</li><li>法人カード</li><li>女性向けカード</li></ul></div>
        <div class="group"><h5 class="orange">年会費</h5>
          <span class="select">指定しない ▼</span></div>
        <div class="group"><h5 class="green">発行会社</h5>
          <ul class="checks"><li>銀行系</li><li>信販系</li><li>流通系</li><li>交通系</li><li>消費者金融系</li><li>その他</li></ul></div>
        <div class="submit">この条件で検索する</div>
        <p class="hit">現在の条件で <b>87枚</b> のカードが該当します</p>
        <p class="search-note">▶ クレジットカード一覧で全てのカードを比較する</p>
      </div>
    </section>

    <section class="box versus">
      <h2 class="sec-head">クレジットカード対決</h2>
      <div class="vs-row"><p class="vs-label">スタンダード<br>カード対決</p>
        <div class="vs-card"><div class="ph" role="img" aria-label="スタンダードカードAの券面"></div>ブルースカイカード<br><span class="detail">詳細を見る</span></div>
        <span class="vs-mark">VS</span>
        <div class="vs-card b"><div class="ph" role="img" aria-label="スタンダードカードBの券面"></div>サンライズカード<br><span class="detail">詳細を見る</span></div></div>
      <div class="vs-row"><p class="vs-label">コンビニで<br>お得な<br>カード対決</p>
        <div class="vs-card"><div class="ph" role="img" aria-label="コンビニ向けカードAの券面"></div>シルバーリーフカード<br><span class="detail">詳細を見る</span></div>
        <span class="vs-mark">VS</span>
        <div class="vs-card b"><div class="ph" role="img" aria-label="コンビニ向けカードBの券面"></div>デイリーマートカード<br><span class="detail">詳細を見る</span></div></div>
      <div class="vs-row"><p class="vs-label">ゴールド<br>カード対決</p>
        <div class="vs-card"><div class="ph" role="img" aria-label="ゴールドカードAの券面"></div>ゴールドリーフカード<br><span class="detail">詳細を見る</span></div>
        <span class="vs-mark">VS</span>
        <div class="vs-card b"><div class="ph" role="img" aria-label="ゴールドカードBの券面"></div>プレミアムサンカード<br><span class="detail">詳細を見る</span></div></div>
      <div class="vs-row"><p class="vs-label">ポイントが<br>貯まり<br>やすいカード</p>
        <div class="vs-card"><div class="ph" role="img" aria-label="ポイントカードAの券面"></div>ポイントプラスカード<br><span class="detail">詳細を見る</span></div>
        <span class="vs-mark">VS</span>
        <div class="vs-card b"><div class="ph" role="img" aria-label="ポイントカードBの券面"></div>スマイルポイントカード<br><span class="detail">詳細を見る</span></div></div>
      <p class="vs-foot">▶ クレジットカード一覧で全てのカードを比較する</p>
    </section>
  </main>

  <aside class="side">
    <div class="ad-platinum" role="img" aria-label="プラチナカードの広告バナー"><span>VELA プラチナカード</span></div>
    <section class="box cat">
      <h2 class="sec-head">カテゴリから探す</h2>
      <h4>目的から探す</h4>
      <ul><li>年会費無料のカード</li><li>ポイント還元率が高いカード</li><li>マイルが貯まるカード</li><li>即日発行できるカード</li><li>海外旅行に強いカード</li><li>電子マネー一体型カード</li><li>ETCカードが無料のカード</li><li>学生向けカード</li></ul>
      <h4>種類から探す</h4>
      <ul><li>一般カード</li><li>ゴールドカード</li><li>プラチナカード</li><li>法人カード</li><li>女性向けカード</li></ul>
      <div class="brand-tiles"><div>VELA</div><div>MERIDIAN</div><div>KSN</div><div>Atlas Prestige</div></div>
    </section>
    <div class="ad-campaign" role="img" aria-label="新規入会キャンペーンの広告バナー"><span>新規入会で最大</span><b>15,000円分</b><span>ポイントプレゼント</span></div>
    <section class="box rank">
      <h2 class="sec-head">ライフスタイル別ランキング</h2>
      <ul>
        <li><span class="no">1</span><div class="ph" role="img" aria-label="カード券面"></div><span><strong>主婦におすすめ</strong>スーパーでポイント2倍</span></li>
        <li><span class="no">2</span><div class="ph" role="img" aria-label="カード券面"></div><span><strong>会社員におすすめ</strong>ランチ代もポイントに</span></li>
        <li><span class="no">3</span><div class="ph" role="img" aria-label="カード券面"></div><span><strong>学生におすすめ</strong>年会費ずっと無料</span></li>
        <li><span class="no">4</span><div class="ph" role="img" aria-label="カード券面"></div><span><strong>旅行好きにおすすめ</strong>マイルが貯まりやすい</span></li>
        <li><span class="no">5</span><div class="ph" role="img" aria-label="カード券面"></div><span><strong>車好きにおすすめ</strong>ガソリン代が割引に</span></li>
        <li><span class="no">6</span><div class="ph" role="img" aria-label="カード券面"></div><span><strong>ネット派におすすめ</strong>通販でポイント3倍</span></li>
      </ul>
    </section>
    <div class="ad-gold">
      <p>ワンランク上のステータスを</p>
      <div class="ph" role="img" aria-label="ゴールドカードの広告写真"></div>
      <p class="name">Atlas Prestige Gold Card</p>
    </div>
  </aside>
</div>

<p class="pagetop">▲ページトップへ</p>
<section class="about">
  <div>
    <h6>カード選びナビ広場について</h6>
    <p>カード選びナビ広場は、各社のクレジットカードを年会費・ポイント・特典などの条件で比較できる情報サイトです。掲載情報は定期的に更新していますが、最新の内容は各カード会社の公式サイトでご確認ください。</p>
  </div>
  <div class="share"><span></span><span></span><span></span></div>
</section>

<footer class="site-footer">
  <div class="footer-inner">
    <ul><li>運営者情報</li><li>プライバシーポリシー</li><li>免責事項</li><li>サイトマップ</li><li>お問い合わせ</li></ul>
    <small>Copyright © 2008-2013 カード選びナビ広場 All Rights Reserved.</small>
  </div>
</footer>
</body>
</html>
```